Agricultural and Earthmoving business card design

We need a business card design for a new company based in Kilmore, Victoria. We are a versatile company with two specialties, the first is an earthworks side, we do big and small jobs, from soccer fields for councils and football clubs down to house cuts for the public, horse ridding arena's, tennis courts and drainage are also small jobs we have experience in. Not only do we do earthmoving, but we also have a lot of experience in the agricultural side of machinery work, from pasture improvements to a lot of experience in hay contracting. We need a business card that doesn't focus on only one side of our business but blends both skills. We would like a primarily black business card that incorporates our company logo. Our company colours are black red , grey and white.

Industry/Entity Type

House

Contact Information for Business Card

Marwick Contracting, Dale Marwick, 2741 Ferngate Rd Kilmore Vic 3764, Phone: 03 5926 4083, Mobile: 0437 902 618. Specialising in Earthmoving, synthetic and natural turf, landscaping, drainage. Also specialising in Agricultural improvements and hay contracting.

Requirements
Must have
• A good blend of both earthmoving and agricultural contracting. Company logo.

```html
<!DOCTYPE html>
<html lang="en">
<head>
<meta charset="utf-8">
<title>Marwick Contracting – Business Card</title>
<link rel="stylesheet" href="https://fonts.googleapis.com/css2?family=Archivo:wght@700&family=Questrial&display=swap">
<style>
  :root {
    --backdrop: #9b9c9e;
    --card-black: #030303;
    --card-red: #ec1f27;
    --ink-dark: #2a2223;
    --ink-red: #e8303a;
    --icon-dark: #3a2a2b;
  }
  * { box-sizing: border-box; margin: 0; padding: 0; }
  html, body {
    width: 1200px;
    height: 1000px;
    overflow: hidden;
    background: var(--backdrop);
  }
  .card {
    position: absolute;
    width: 620px;
    height: 400px;
    border-radius: 26px;
    overflow: hidden;
    background: var(--card-black);
    box-shadow: 0 18px 40px rgba(0,0,0,0.28);
  }
  .card--front { left: 142px; top: 92px; }
  .card--back  { left: 478px; top: 520px; }

  .brand {
    position: absolute;
    left: 0; right: 0;
    display: flex;
    align-items: center;
    justify-content: center;
    gap: 14px;
  }
  .brand__mark {
    width: 22px;
    height: 22px;
    background: var(--ink-red);
  }
  .brand__name {
    font-family: "Archivo", sans-serif;
    font-weight: 700;
    color: var(--ink-red);
    text-transform: uppercase;
    letter-spacing: 0.5px;
  }
  .card--front .brand { top: 220px; }
  .card--front .brand__name { font-size: 30px; }
  .card--front .brand__mark { width: 28px; height: 28px; }

  .front__band {
    position: absolute;
    left: 0; right: 0; bottom: 0;
    height: 96px;
    background: var(--card-red);
    display: flex;
    align-items: center;
    justify-content: center;
  }
  .front__tagline {
    font-family: "Archivo", sans-serif;
    font-weight: 700;
    font-size: 18px;
    color: var(--ink-dark);
    letter-spacing: 0.4px;
  }

  .back__wave { position: absolute; inset: 0; }
  .card--back .brand { top: 138px; }
  .card--back .brand__name { font-size: 22px; }

  .back__person {
    position: absolute;
    left: 78px;
    top: 266px;
    font-family: "Questrial", sans-serif;
    font-size: 20px;
    color: var(--ink-dark);
    text-transform: uppercase;
    letter-spacing: 1px;
  }
  .contact-list {
    position: absolute;
    left: 296px;
    top: 214px;
    list-style: none;
  }
  .contact-list li {
    display: flex;
    align-items: center;
    gap: 7px;
    height: 24px;
    font-family: "Questrial", sans-serif;
    font-size: 16px;
    color: var(--ink-dark);
  }
  .contact-list svg { width: 18px; height: 18px; flex: none; }
  .back__address {
    position: absolute;
    left: 70px;
    bottom: 36px;
    font-family: "Questrial", sans-serif;
    font-size: 18px;
    color: var(--ink-dark);
    letter-spacing: 0.5px;
  }
</style>
</head>
<body>

<section class="card card--front">
  <div class="brand">
    <span class="brand__mark"></span>
    <span class="brand__name">Marwick Contracting</span>
  </div>
  <div class="front__band">
    <p class="front__tagline">EARTHMOVING AND AGRICULTURAL CONTRACTING</p>
  </div>
</section>

<section class="card card--back">
  <svg class="back__wave" viewBox="0 0 620 400" preserveAspectRatio="none">
    <path d="M0 212 C 120 196, 230 172, 360 176 C 460 180, 540 172, 620 150 L620 400 L0 400 Z" fill="var(--card-red)"/>
  </svg>
  <div class="brand">
    <span class="brand__mark"></span>
    <span class="brand__name">Marwick Contracting</span>
  </div>

  <p class="back__person">Dale Marwick</p>

  <ul class="contact-list">
    <li>
      <svg viewBox="0 0 16 16"><rect width="16" height="16" rx="2" fill="var(--icon-dark)"/><path d="M4.5 3.5 L6.5 3.5 L7.2 6 L6 7 Q7 9.2 9 10 L10 8.8 L12.5 9.5 L12.5 11.5 Q7 12.5 4.5 3.5Z" fill="var(--card-red)"/></svg>
      03 5926 4083
    </li>
    <li>
      <svg viewBox="0 0 16 16"><rect width="16" height="16" rx="2" fill="var(--icon-dark)"/><rect x="5.5" y="2.5" width="5" height="11" rx="1" fill="var(--card-red)"/><rect x="6.5" y="4" width="3" height="6" fill="var(--icon-dark)"/></svg>
      0437 902 618
    </li>
    <li>
      <svg viewBox="0 0 16 16"><rect width="16" height="16" rx="2" fill="var(--icon-dark)"/><rect x="3" y="4.5" width="10" height="7" fill="var(--card-red)"/><path d="M3 4.5 L8 8.5 L13 4.5" stroke="var(--icon-dark)" fill="none"/></svg>
      dale@marwickcontracting.com.au
    </li>
    <li>
      <svg viewBox="0 0 16 16"><rect width="16" height="16" rx="2" fill="var(--icon-dark)"/><circle cx="8" cy="8" r="4.5" fill="none" stroke="var(--card-red)"/><ellipse cx="8" cy="8" rx="2" ry="4.5" fill="none" stroke="var(--card-red)"/><path d="M3.5 8 H12.5" stroke="var(--card-red)"/></svg>
      www.marwickcontracting.com.au
    </li>
  </ul>

  <p class="back__address">2741 Ferngate Rd, Ashvale Vic 3841</p>
</section>

</body>
</html>
```